4K Business Card Design

We need a business card that emphasizes consulting services worldwide. The name of the company is KKKK Consulting Group. We provide consulting services across several industries including but not limited to commodities, telecom, manufacturing, logistics, marketing and operations. We would like to see a creative design that emphasizes the global aspect, including Latin America and US markets, as well the bilingual nature of the service offerings.

The contact information section should include icons to represent the following data:
1) Name, Title and Company Name
2) Mobile Number
3) Skype ID
4) Email
5) Web Page
6) Location

We would like to see a card that emphasizes the worldwide concept. The back of the card should be simple, including only the logo (or a portion of the logo) and the slogan.

We would also like to see business cards in a booklet format. The colors to be used should be the same combination of colors used in the logos attached to this brief.

The logo design and some business card examples from Artful Herd are attached for reference on style and look.

Target Market(s)

International business executives, 45-65 years of age, bilingual

Industry/Entity Type

Marketing

Colors
0792cd
34a7d8
85cae6
ffffff
cee9f5
ecf7fb

Requirements
Must have
• Please follow colors in logo attached.

2) Mobile Number
3) Skype ID
4) Email
5) Web Page
6) Location
Nice to have
• Global concept, consulting profile, diverse industry focus
Should not have
• No black color

```html
<!DOCTYPE html>
<html lang="en">
<head>
<meta charset="utf-8">
<title>KKKK Consulting Group – Business Card</title>
<link rel="stylesheet" href="https://fonts.googleapis.com/css2?family=Cinzel:wght@500&family=Josefin+Sans:wght@400;600&display=swap">
<style>
  :root {
    --stage: #c9ccce;
    --card: #ffffff;
    --blue-deep: #0792cd;
    --blue-mid: #34a7d8;
    --blue-soft: #85cae6;
    --blue-pale: #cee9f5;
    --blue-mist: #ecf7fb;
    --slate: #6f8a96;
  }
  * { margin: 0; padding: 0; box-sizing: border-box; }
  html, body { width: 1200px; height: 900px; overflow: hidden; }
  body {
    background: var(--stage);
    font-family: "Josefin Sans", "Gill Sans", sans-serif;
    position: relative;
  }
  .card {
    position: absolute;
    left: 300px;
    width: 600px;
    height: 343px;
    background: var(--card);
    overflow: hidden;
    box-shadow: 0 6px 18px rgba(60, 70, 80, 0.25);
  }
  .card--back { top: 48px; }
  .card--front { top: 470px; border-bottom: 8px solid var(--blue-soft); }

  .faint-square {
    position: absolute;
    background: var(--blue-soft);
    opacity: 0.35;
  }
  .card--back .faint-square { right: 30px; bottom: 36px; width: 110px; height: 110px; }
  .card--front .faint-square { right: 36px; bottom: 26px; width: 120px; height: 120px; }

  .back-mark {
    position: absolute;
    top: 118px;
    left: 0; right: 0;
    text-align: center;
  }
  .back-mark .mark-square {
    display: block;
    width: 34px; height: 34px;
    margin: 0 auto 18px;
    background: var(--blue-soft);
  }
  .back-mark .company-name {
    font-family: "Cinzel", serif;
    font-weight: 500;
    font-size: 30px;
    letter-spacing: 1px;
    color: var(--slate);
  }

  .front-mark {
    position: absolute;
    top: 34px;
    right: 36px;
    display: flex;
    align-items: center;
    gap: 12px;
  }
  .front-mark .mark-square {
    width: 26px; height: 26px;
    background: var(--blue-soft);
  }
  .front-mark .company-name {
    font-weight: 600;
    font-size: 25px;
    letter-spacing: 1.5px;
    color: var(--slate);
    text-transform: uppercase;
  }

  .contact {
    position: absolute;
    top: 110px;
    left: 34px;
    width: 300px;
    color: var(--blue-mid);
  }
  .contact .person-name {
    font-size: 23px;
    font-weight: 400;
    letter-spacing: 1px;
    color: var(--blue-deep);
    text-transform: uppercase;
    line-height: 1;
  }
  .contact .person-title {
    font-size: 9px;
    letter-spacing: 1.2px;
    text-transform: uppercase;
    color: var(--blue-mid);
    margin-top: 3px;
  }
  .contact .rule {
    border: 0;
    border-top: 1px dotted var(--blue-mid);
    margin: 8px 0 10px;
  }
  .contact-list { list-style: none; }
  .contact-list li {
    display: flex;
    align-items: center;
    gap: 10px;
    font-size: 14px;
    line-height: 24px;
    color: var(--blue-mid);
  }
  .contact-list svg { width: 14px; height: 14px; flex: none; }
  .location {
    font-size: 14px;
    color: var(--blue-mid);
    margin-top: 2px;
  }
</style>
</head>
<body>

  <section class="card card--back" aria-label="Card back">
    <div class="back-mark">
      <span class="mark-square"></span>
      <span class="company-name">KKKK Consulting Group</span>
    </div>
    <div class="faint-square"></div>
  </section>

  <section class="card card--front" aria-label="Card front">
    <div class="front-mark">
      <span class="mark-square"></span>
      <span class="company-name">KKKK Consulting Group</span>
    </div>

    <div class="contact">
      <p class="person-name">Lucía Ferrand</p>
      <p class="person-title">President &amp; CEO</p>
      <hr class="rule">
      <ul class="contact-list">
        <li>
          <svg viewBox="0 0 14 14" aria-hidden="true"><rect x="3" y="0.5" width="8" height="13" rx="1.5" fill="var(--blue-deep)"/><rect x="4.5" y="2" width="5" height="8" fill="#fff"/></svg>
          : +1 305 555-0147
        </li>
        <li>
          <svg viewBox="0 0 14 14" aria-hidden="true"><rect x="0.5" y="2.5" width="13" height="9" fill="var(--blue-deep)"/><path d="M1 3 L7 8 L13 3" stroke="#fff" stroke-width="1.2" fill="none"/></svg>
          : k4cg@mailharbor.com
        </li>
        <li>
          <svg viewBox="0 0 14 14" aria-hidden="true"><circle cx="7" cy="7" r="6.5" fill="var(--blue-deep)"/></svg>
          : k4consultinggroup
        </li>
      </ul>
      <hr class="rule">
      <p class="location">Bayview Isles, FL</p>
    </div>

    <div class="faint-square"></div>
  </section>

</body>
</html>
```